The 90s Were Bright Static

We need a CD cover design for a Band EP, The Band is called Velko. The EP is called "The 90s Were Bright Static" Taking Inspiration from all things growing up in the 90s. The name is a nod to YouthBeam programming block that airs throwback to classic shows from the 90s. Attaching some stills from the video that is inspired from colors in early 90's HipHop Videos for the vibe we are after. Band Photo's not needed in EP cover.
Updates

Target Market(s)

Blog Music Lovers. 18-35 😈😑😇

Font styles to use
Other font styles liked:
• Quiet Baron "TV Show" style

Requirements
Must have
• Creative with a nod to the 90s. Inspired by classic US TV shows and music.

```html
<!DOCTYPE html>
<html lang="en">
<head>
<meta charset="utf-8">
<title>Velko – The 90s Were Bright Static</title>
<link rel="stylesheet" href="https://fonts.googleapis.com/css2?family=Audiowide&display=swap">
<style>
  :root {
    --backdrop: #f2f2f4;
    --pink: #ea6fe6;
    --magenta: #d95fc9;
    --violet: #8a66b8;
    --rose: #e07aa8;
    --lime: #8fd13a;
    --lime-deep: #6aa82a;
    --sky: #7aaee8;
  }
  * { margin: 0; padding: 0; box-sizing: border-box; }
  html, body {
    width: 1200px;
    height: 988px;
    overflow: hidden;
    background: var(--backdrop);
  }
  .cover {
    position: absolute;
    left: 160px;
    top: 54px;
    width: 880px;
    height: 880px;
    overflow: hidden;
  }
  .cover-art {
    position: absolute;
    inset: 0;
    background:
      radial-gradient(circle at 50% 52%, var(--rose) 0%, var(--violet) 12%, var(--pink) 26%, var(--magenta) 42%, var(--violet) 55%, var(--pink) 68%, var(--magenta) 85%, var(--violet) 100%);
  }
  .ep-title {
    position: absolute;
    left: 50%;
    top: 46%;
    transform: translate(-50%, -50%) rotate(-42deg);
    font-family: "Audiowide", sans-serif;
    font-size: 78px;
    line-height: 1.05;
    text-transform: uppercase;
    text-align: center;
    white-space: nowrap;
    color: var(--lime);
    -webkit-text-stroke: 3px var(--lime-deep);
    text-shadow: 0 0 18px var(--sky), 0 0 36px var(--sky);
  }
  .band-name {
    position: absolute;
    right: 44px;
    bottom: 40px;
    font-family: "Audiowide", sans-serif;
    font-size: 74px;
    text-transform: uppercase;
    color: var(--lime);
    -webkit-text-stroke: 3px var(--lime-deep);
    text-shadow: 0 0 16px var(--sky), 0 0 30px var(--sky);
  }
</style>
</head>
<body>
  <main class="cover">
    <div class="cover-art" role="img" aria-label="Psychedelic pink and violet web-like tunnel pattern radiating from the centre"></div>
    <h1 class="ep-title">The 90s Were<br>Bright Static</h1>
    <p class="band-name">Velko</p>
  </main>
</body>
</html>
```